Australian wine project aimed at the Asian market

We are looking for a wine label that is attractive to the Asian market specifically mainland China. There should be space left for varietal and alcohol by % info. The products will be red and sparkling red the label should reflect the country of origin but must be elegant.
Reason: The first brief was a bit vague.
Target Market(s)
Adults based in China with a leaning towards traditional design.
Requirements
Must have
- I would love to see a pen and ink style of design incorporating a traditional Australian homestead. It would be great to see a Kangaroo if possible encroaching on the land.

```html
<!DOCTYPE html>
<html lang="en">
<head>
<meta charset="utf-8">
<title>Meridian Estate – Pinot Noir 2012 Label</title>
<link rel="stylesheet" href="https://fonts.googleapis.com/css2?family=Cormorant+SC:wght@400;500&family=Cormorant+Garamond:ital,wght@0,400;0,500;1,600;1,700&display=swap">
<style>
  :root {
    --backdrop: #0a0b0d;
    --paper: #f0eee7;
    --paper-edge: #e6e3da;
    --gold: #a6873a;
    --ink: #1c1b19;
    --ink-soft: #3a3936;
    --wash-light: #d9d8d4;
    --wash-dark: #8e8d89;
    --map-tone: #d2d0c9;
  }
  * { margin: 0; padding: 0; box-sizing: border-box; }
  html, body {
    width: 1200px; height: 1200px; overflow: hidden;
    background: var(--backdrop);
  }
  .canvas { position: relative; width: 1200px; height: 1200px; }

  .brand-badge {
    position: absolute; left: 150px; top: 262px;
    display: flex; align-items: center; gap: 10px;
    font-family: "Cormorant Garamond", serif; font-weight: 500; font-size: 15px;
    color: var(--gold); white-space: nowrap;
  }
  .brand-badge__dot {
    width: 14px; height: 14px; border-radius: 50%; background: var(--gold);
  }

  .label {
    position: absolute; top: 370px; height: 490px;
    background: radial-gradient(ellipse at 50% 45%, var(--paper) 55%, var(--paper-edge) 100%);
    color: var(--ink);
  }
  .label--front { left: 143px; width: 536px; }
  .label--back { left: 745px; width: 352px; }

  .brand-name {
    position: absolute; font-family: "Cormorant Garamond", serif; font-weight: 500;
    color: var(--gold); white-space: nowrap; letter-spacing: 1px;
  }
  .dotted-rule { position: absolute; height: 0; border-top: 2px dotted var(--ink-soft); }

  .front-title { left: 0; right: 0; top: 52px; text-align: center; font-size: 40px; }
  .label--front .dotted-rule { left: 89px; width: 357px; top: 103px; }
  .front-variety {
    position: absolute; left: 0; right: 0; top: 108px; text-align: center;
    font-family: "Cormorant SC", serif; font-size: 18px; line-height: 19px;
  }
  .front-vintage {
    position: absolute; left: 0; right: 0; top: 126px; text-align: center;
    font-family: "Cormorant SC", serif; font-size: 14px;
  }
  .homestead-art {
    position: absolute; left: 103px; top: 184px; width: 312px; height: 208px;
    background: radial-gradient(ellipse at 50% 55%, var(--wash-dark) 0%, var(--wash-light) 55%, rgba(240,238,231,0) 75%);
  }
  .front-alcohol {
    position: absolute; left: 33px; top: 420px;
    font-family: "Cormorant SC", serif; font-size: 15px; line-height: 16px;
  }
  .front-volume {
    position: absolute; right: 33px; top: 440px;
    display: flex; align-items: baseline; gap: 6px;
    font-family: "Cormorant SC", serif; font-size: 14px;
  }
  .front-volume .mini-brand {
    font-family: "Cormorant Garamond", serif; font-weight: 500; font-size: 11px;
  }

  .back-title { left: 29px; top: 18px; font-size: 23px; }
  .label--back .dotted-rule { left: 29px; width: 298px; top: 58px; }
  .back-heading {
    position: absolute; left: 29px; top: 74px;
    font-family: "Cormorant SC", serif; font-size: 31px; line-height: 32px; font-weight: 400;
  }
  .back-subheading {
    position: absolute; left: 29px; top: 104px;
    font-family: "Cormorant Garamond", serif; font-style: italic; font-weight: 700; font-size: 22px;
  }
  .back-description {
    position: absolute; left: 29px; width: 298px; top: 146px;
    font-family: "Cormorant Garamond", serif; font-weight: 500; font-size: 13.4px; line-height: 20.7px;
    text-align: justify; color: var(--ink);
  }
  .back-notes {
    position: absolute; left: 29px; width: 156px; top: 350px;
    font-family: "Cormorant SC", serif; font-size: 10.2px; line-height: 15.4px;
    text-align: justify; color: var(--ink);
  }
  .region-caption {
    position: absolute; left: 199px; top: 348px;
    font-family: "Cormorant Garamond", serif; font-weight: 500; font-size: 12px;
  }
  .region-map {
    position: absolute; left: 205px; top: 370px; width: 116px; height: 100px;
    background: radial-gradient(ellipse at 50% 50%, var(--map-tone) 0%, rgba(240,238,231,0) 72%);
  }
  .region-marker {
    position: absolute; left: 286px; top: 428px; width: 7px; height: 7px;
    border-radius: 50%; background: var(--gold);
  }
</style>
</head>
<body>
<main class="canvas">
  <div class="brand-badge"><span class="brand-badge__dot"></span>Meridian Estate</div>

  <section class="label label--front">
    <h1 class="brand-name front-title">Meridian Estate</h1>
    <div class="dotted-rule"></div>
    <p class="front-variety">Pinot noir</p>
    <p class="front-vintage">2012</p>
    <div class="homestead-art" role="img" aria-label="Pen and ink wash illustration of a traditional Australian homestead with a tree, set over a faint map of Australia"></div>
    <p class="front-alcohol">Alc:<br>12% vol</p>
    <p class="front-volume"><span class="mini-brand">Meridian</span><span>0.75L</span></p>
  </section>

  <section class="label label--back">
    <h2 class="brand-name back-title">Meridian Estate</h2>
    <div class="dotted-rule"></div>
    <h3 class="back-heading">Pinot noir 2012</h3>
    <p class="back-subheading">Premium wine</p>
    <p class="back-description">Lorem ipsum dolor sit amet, consectetuer adipiscing elit. Aenean commodo ligula eget dolor. Aenean massa. Cum sociis natoque penatibus et magnis dis parturient montes, nascetur ridiculus mus. Donec quam felis, ultricies nec, pellentesque eu, pretium quis, sem. Nulla consequat massa quis enim. Donec pede justo, fringilla vel, aliquet nec, vulputate eget, arcu. In enim justo, rhoncus ut, imperdiet a, venenatis vitae, justo. Nullam dictum felis eu pede mollis pretium. Integer tincidunt. Cras dapibus.</p>
    <p class="back-notes">Lorem ipsum dolor sit amet, consectetuer adipiscing elit. Aenean commodo ligula eget dolor. Aenean massa. Cum sociis natoque penatibus et magnis dis parturient montes, nascetur ridicu</p>
    <p class="region-caption">Wine region :</p>
    <div class="region-map" role="img" aria-label="Outline map of Australia showing the wine region"></div>
    <span class="region-marker"></span>
  </section>
</main>
</body>
</html>
```